Talvor GmbH business card

We Talvor GmbH based in Switzerland are looking for a business card design. The Fresh Jung, appealing to customers of all kinds. We already have a logo to upload but still a business card. Details: Talvor GmbH Address: Lindenweg 14b in 9476 Brugwil. Tel: 41 79 462 37 18, web: Talvor.ch, E-mail: info@Talvor.ch Facebook: Talvor GmbH. I am the Managing Director: Luka Petrovac. On reverse: Title: Transporter and bus rental Gross: Without deposit Super prices
Contact Information for Business Card
Siehe Projektbeschreibung
Requirements
Should not have
- Other pictures

```html
<!DOCTYPE html>
<html lang="en">
<head>
<meta charset="utf-8">
<title>Talvor GmbH – Business Card</title>
<link rel="stylesheet" href="https://fonts.googleapis.com/css2?family=Lato:wght@400;700;900&display=swap">
<style>
  :root {
    --navy: #262469;
    --slate: #7e98b1;
    --paper: #ffffff;
    --stage: #222222;
  }
  * { margin: 0; padding: 0; box-sizing: border-box; }
  html, body { width: 1189px; height: 1200px; overflow: hidden; background: var(--stage); }
  body { position: relative; font-family: "Lato", Arial, sans-serif; }

  .card {
    position: absolute;
    left: 171px;
    width: 855px;
    height: 488px;
    box-shadow: 0 2px 6px rgba(0,0,0,.5);
    overflow: hidden;
  }
  .card--front { top: 67px; background: var(--navy); }
  .card--back { top: 626px; background: var(--paper); }

  .brand {
    position: absolute;
    left: 0; right: 0;
    display: flex;
    align-items: center;
    justify-content: center;
    gap: 18px;
    font-weight: 900;
    font-size: 84px;
    letter-spacing: 2px;
    line-height: 1;
  }
  .brand__mark { width: 58px; height: 58px; }
  .card--front .brand { top: 200px; color: var(--paper); }
  .card--front .brand__mark { background: var(--paper); }
  .card--back .brand { top: 110px; color: var(--navy); }
  .card--back .brand__mark { background: var(--navy); }

  .person {
    position: absolute;
    right: 439px;
    top: 302px;
    text-align: right;
    color: var(--navy);
  }
  .person__name { font-weight: 700; font-size: 29px; line-height: 30px; }
  .person__role { color: var(--slate); font-size: 23px; line-height: 24px; }
  .person__address { margin-top: 12px; font-size: 23px; line-height: 24px; }

  .divider {
    position: absolute;
    left: 416px;
    top: 302px;
    width: 2px;
    height: 112px;
    background: var(--slate);
  }

  .contacts {
    position: absolute;
    left: 439px;
    top: 300px;
    list-style: none;
    color: var(--navy);
    font-size: 23px;
  }
  .contacts li { display: flex; align-items: center; height: 29px; }
  .contacts svg { width: 24px; height: 24px; margin-right: 9px; flex: none; }

  .stripe { position: absolute; bottom: 0; height: 19px; }
  .stripe--navy { left: 0; width: 424px; background: var(--navy); }
  .stripe--slate { left: 424px; right: 0; background: var(--slate); }
</style>
</head>
<body>
  <section class="card card--front">
    <div class="brand"><span class="brand__mark"></span>Talvor</div>
  </section>

  <section class="card card--back">
    <div class="brand"><span class="brand__mark"></span>Talvor</div>

    <div class="person">
      <p class="person__name">LUKA PETROVAC</p>
      <p class="person__role">Managing Director</p>
      <p class="person__address">Lindenweg 14b<br>9476 Brugwil, Switzerland</p>
    </div>

    <div class="divider"></div>

    <ul class="contacts">
      <li>
        <svg viewBox="0 0 24 24" aria-hidden="true"><rect width="24" height="24" fill="#7e98b1"/><path d="M5 10c0-3 14-3 14 0v1h-4v-2h-6v2H5z M7 13h10l1 6H6z" fill="#fff"/></svg>
        41 79 462 37 18
      </li>
      <li>
        <svg viewBox="0 0 24 24" aria-hidden="true"><rect width="24" height="24" fill="#7e98b1"/><path d="M8 4h8v5H8z M5 10h14v7H5z M8 15h8v5H8z" fill="#fff"/></svg>
        41 71 462 37 19
      </li>
      <li>
        <svg viewBox="0 0 24 24" aria-hidden="true"><rect width="24" height="24" fill="#7e98b1"/><rect x="4" y="6" width="16" height="12" fill="none" stroke="#fff" stroke-width="1.5"/><path d="M4 6l8 7 8-7" fill="none" stroke="#fff" stroke-width="1.5"/></svg>
        info@Talvor.ch
      </li>
      <li>
        <svg viewBox="0 0 24 24" aria-hidden="true"><rect width="24" height="24" fill="#7e98b1"/><circle cx="12" cy="12" r="7" fill="none" stroke="#fff" stroke-width="1.5"/><path d="M5 12h14 M12 5c-4 4-4 10 0 14 M12 5c4 4 4 10 0 14" fill="none" stroke="#fff" stroke-width="1.2"/></svg>
        www.Talvor.ch
      </li>
    </ul>

    <div class="stripe stripe--navy"></div>
    <div class="stripe stripe--slate"></div>
  </section>
</body>
</html>
```